Local Flower Farm Needs Business Card Design

I need business cards designed for a flower farm based in Eudora, Kansas.
Business Info:
We are a local cut flower farm located in Eudora, Kansas, founded by Darla Hoffstrom. What started as a passion for agriculture and search for more joy in daily life has blossomed into a small business dedicated to providing the community with beautiful, fresh, and sustainable flowers. We specialize in local, seasonal blooms, ensuring that every petal reflects the care and dedication we pour into our craft. Our mission is to deliver the highest quality flowers directly to our customers through local farmers markets and to florists who share our commitment to sustainability. Join us in celebrating the beauty of nature, one bloom at a time!
Contact Details:
Darla Hoffstrom
Owner
Phone 913-555-0147
Facebook: Lorabelle Quinn Blossoms
Instagram: @LorabelleQuinnBlossoms
Website: LorabelleQuinnBlossoms.example
Target Market(s)
Wholesale to Florists and Direct to Consumer via Farmers Market
Industry/Entity Type
Florist, Farm
Contact Information for Business Card
Name, Contact Info, Logo
Look and feel

```html
<!DOCTYPE html>
<html lang="en">
<head>
<meta charset="utf-8">
<title>Lorabelle Quinn Blossoms – Business Card</title>
<link rel="stylesheet" href="https://fonts.googleapis.com/css2?family=Nunito+Sans:wght@400;600;700;800&display=swap">
<style>
  :root {
    --canvas-bg: #a7a7a7;
    --card-white: #ffffff;
    --ink: #10292f;
    --deep-teal: #0f2a30;
    --on-dark: #ffffff;
  }
  * { box-sizing: border-box; margin: 0; padding: 0; }
  html, body {
    width: 1200px;
    height: 1200px;
    overflow: hidden;
    background: var(--canvas-bg);
    font-family: "Nunito Sans", sans-serif;
  }
  .canvas { position: relative; width: 1200px; height: 1200px; }

  .card {
    position: absolute;
    left: 152px;
    width: 896px;
    height: 523px;
  }
  .card--front { top: 52px; background: var(--card-white); color: var(--ink); }
  .card--back { top: 616px; background: var(--deep-teal); color: var(--on-dark); }

  .owner {
    position: absolute;
    left: 70px;
    top: 203px;
  }
  .owner__name {
    font-size: 30px;
    font-weight: 700;
    letter-spacing: 0.3px;
    text-transform: uppercase;
    line-height: 1.1;
  }
  .owner__role {
    margin-top: 8px;
    font-size: 22px;
    font-weight: 400;
    line-height: 1.2;
  }

  .contact-list {
    position: absolute;
    left: 72px;
    top: 318px;
    list-style: none;
  }
  .contact-list__item {
    display: flex;
    align-items: center;
    height: 38px;
    font-size: 22px;
    font-weight: 400;
  }
  .contact-list__item--web { font-weight: 700; }
  .contact-list__icon {
    width: 18px;
    height: 18px;
    margin-right: 22px;
    flex: none;
  }

  .brand-seal {
    position: absolute;
    width: 268px;
    height: 268px;
    display: flex;
    align-items: center;
    justify-content: center;
    text-align: center;
  }
  .card--front .brand-seal { left: 539px; top: 76px; }
  .card--back .brand-seal { left: 314px; top: 125px; }
  .brand-seal__ring {
    position: absolute;
    inset: 0;
    border-radius: 50%;
    border: 1.5px solid currentColor;
  }
  .brand-seal__name {
    font-size: 22px;
    font-weight: 600;
    letter-spacing: 2px;
    line-height: 1.35;
    text-transform: uppercase;
  }
</style>
</head>
<body>
<main class="canvas">

  <section class="card card--front" aria-label="Business card front">
    <div class="owner">
      <h1 class="owner__name">Darla Hoffstrom</h1>
      <p class="owner__role">Owner</p>
    </div>

    <ul class="contact-list">
      <li class="contact-list__item">
        <svg class="contact-list__icon" viewBox="0 0 24 24" aria-hidden="true">
          <path fill="currentColor" d="M6.6 10.8a15.1 15.1 0 0 0 6.6 6.6l2.2-2.2a1 1 0 0 1 1-.25 11.4 11.4 0 0 0 3.6.57 1 1 0 0 1 1 1V20a1 1 0 0 1-1 1A17 17 0 0 1 3 4a1 1 0 0 1 1-1h3.5a1 1 0 0 1 1 1c0 1.25.2 2.45.57 3.57a1 1 0 0 1-.25 1z"/>
        </svg>
        913-555-0147
      </li>
      <li class="contact-list__item">
        <svg class="contact-list__icon" viewBox="0 0 24 24" aria-hidden="true">
          <circle cx="12" cy="12" r="6" fill="currentColor"/>
        </svg>
        Lorabelle Quinn Blossoms
      </li>
      <li class="contact-list__item">
        <svg class="contact-list__icon" viewBox="0 0 24 24" aria-hidden="true">
          <circle cx="12" cy="12" r="6" fill="currentColor"/>
        </svg>
        @LorabelleQuinnBlossoms
      </li>
      <li class="contact-list__item contact-list__item--web">
        <svg class="contact-list__icon" viewBox="0 0 24 24" aria-hidden="true">
          <g fill="none" stroke="currentColor" stroke-width="2">
            <circle cx="12" cy="12" r="9"/>
            <ellipse cx="12" cy="12" rx="4" ry="9"/>
            <line x1="3" y1="12" x2="21" y2="12"/>
          </g>
        </svg>
        LorabelleQuinnBlossoms.example
      </li>
    </ul>

    <div class="brand-seal">
      <span class="brand-seal__ring" aria-hidden="true"></span>
      <p class="brand-seal__name">Lorabelle<br>Quinn<br>Blossoms</p>
    </div>
  </section>

  <section class="card card--back" aria-label="Business card back">
    <div class="brand-seal">
      <span class="brand-seal__ring" aria-hidden="true"></span>
      <p class="brand-seal__name">Lorabelle<br>Quinn<br>Blossoms</p>
    </div>
  </section>

</main>
</body>
</html>
```